Business Card Design

I need a business card design for a new company based in Sydney called 'The Copper Ladle'. We deliver organic, gourmet and fine foods to your door.

I would like to see creative, unique designs which use colours which represent health and nature like green.

Target Market(s)

Health conscious 20 to 35 year olds.

Industry/Entity Type

Health

Contact Information for Business Card

The Copper Ladle, Owen Barclett, owen@thecopperladle.com.au, 0427685392

Requirements
Must have
• My logo.

```html
<!DOCTYPE html>
<html lang="en">
<head>
<meta charset="utf-8">
<title>The Copper Ladle – Business Card</title>
<link href="https://fonts.googleapis.com/css2?family=Open+Sans:wght@300;400;700&display=swap" rel="stylesheet">
<style>
  :root {
    --page-bg: #e4e5e4;
    --card-bg: #ffffff;
    --leaf-green: #7cc242;
    --forest-green: #3f8a1f;
    --ink: #2b2b2b;
    --muted: #555b55;
  }
  * { box-sizing: border-box; margin: 0; padding: 0; }
  html, body {
    width: 1200px;
    height: 1026px;
    overflow: hidden;
    background: var(--page-bg);
    font-family: "Open Sans", Arial, sans-serif;
  }
  .card-sheet {
    width: 1200px;
    height: 1026px;
    display: flex;
    flex-direction: column;
    align-items: center;
    justify-content: center;
    gap: 30px;
  }
  .card {
    position: relative;
    width: 820px;
    height: 468px;
    background: var(--card-bg);
    box-shadow: 0 2px 10px rgba(0, 0, 0, 0.12);
  }
  .brand {
    position: absolute;
    display: flex;
    align-items: center;
    gap: 16px;
  }
  .brand-dot {
    width: 84px;
    height: 84px;
    border-radius: 50%;
    background: var(--leaf-green);
    flex-shrink: 0;
  }
  .brand-name {
    font-weight: 300;
    font-size: 46px;
    line-height: 1.05;
    color: var(--leaf-green);
  }
  .card-front .brand { left: 160px; top: 180px; }
  .card-back .brand { left: 100px; top: 110px; }
  .accent-band {
    position: absolute;
    left: 42px;
    top: 0;
    bottom: 0;
    width: 16px;
    background: var(--leaf-green);
    border-left: 5px solid var(--forest-green);
  }
  .contact {
    position: absolute;
    left: 92px;
    top: 270px;
  }
  .contact-title {
    font-size: 26px;
    font-weight: 700;
    color: var(--forest-green);
    margin-bottom: 12px;
  }
  .contact-title span { color: var(--ink); }
  .contact-list { list-style: none; }
  .contact-list li {
    display: flex;
    align-items: center;
    gap: 12px;
    font-size: 20px;
    color: var(--muted);
    line-height: 31px;
  }
  .contact-list svg {
    width: 16px;
    height: 16px;
    flex-shrink: 0;
    fill: var(--forest-green);
  }
</style>
</head>
<body>
<main class="card-sheet">
  <section class="card card-front">
    <div class="brand">
      <span class="brand-dot"></span>
      <span class="brand-name">The Copper<br>Ladle</span>
    </div>
  </section>

  <section class="card card-back">
    <div class="accent-band"></div>
    <div class="brand">
      <span class="brand-dot"></span>
      <span class="brand-name">The Copper<br>Ladle</span>
    </div>
    <div class="contact">
      <h2 class="contact-title">Contact <span>Me</span></h2>
      <ul class="contact-list">
        <li>
          <svg viewBox="0 0 16 16" aria-hidden="true"><path d="M4 1h2.5l1 3.5-1.6 1.2a8 8 0 0 0 4.4 4.4l1.2-1.6 3.5 1V12c0 1.7-1.3 3-3 3A11 11 0 0 1 1 4c0-1.7 1.3-3 3-3z"/></svg>
          0427685392
        </li>
        <li>
          <svg viewBox="0 0 16 16" aria-hidden="true"><path d="M1 3h14v10H1V3zm1.5 1.8V11.5h11V4.8L8 8.8 2.5 4.8z"/></svg>
          owen@thecopperladle.com.au
        </li>
        <li>
          <svg viewBox="0 0 16 16" aria-hidden="true"><path fill-rule="evenodd" d="M8 1a7 7 0 1 1 0 14A7 7 0 0 1 8 1zm0 1.4A5.6 5.6 0 1 0 8 13.6 5.6 5.6 0 0 0 8 2.4zM7.3 2.6h1.4v10.8H7.3zM2.6 7.3h10.8v1.4H2.6z"/></svg>
          www.copperladle.example
        </li>
      </ul>
    </div>
  </section>
</main>
</body>
</html>
```